Downloadable PDF "Brochure?"

We have a Free download we will provide in exchange for an email address on our new Trailmark website. The website at www.venturetrailmark-example.com is in development and will look nothing like what it currently does, but you can go there and get a sense of what Trailmark is from the text on the website. (see the attached image 'site design' for the new redesigned website for aesthetics).

We are looking for a nice design for the document, that will represent the mostly text document well. We are not actually looking to print these at a printer so they don't have to be print ready. I went ahead and included the logo and colors and fonts file again just for reference.

Target Market(s)

Business Owners / Decision Makers

Requirements
Must have
• See attached document 'trailmark freebie' for text to be utilized in the finished deliverable.
• See the attached image 'Site Design' for the website aesthetic.

```html
<!DOCTYPE html>
<html lang="en">
<head>
<meta charset="utf-8">
<title>Trailmark – 10 Questions To Choose The Best Technology Advisor</title>
<link rel="stylesheet" href="https://fonts.googleapis.com/css2?family=Cinzel:wght@600;700&family=Open+Sans:ital,wght@0,400;0,700;1,700&display=swap">
<style>
:root{
  --orange:#c7693e;
  --slate:#2f3d47;
  --ink:#2b2b2b;
  --paper:#ffffff;
  --backdrop:#ebebec;
}
*{box-sizing:border-box;margin:0;padding:0}
html,body{width:1200px;height:1200px;overflow:hidden;background:var(--backdrop)}
body{position:relative;font-family:"Open Sans",sans-serif;color:var(--ink)}
.page{position:absolute;width:390px;height:505px;background:var(--paper);overflow:hidden;box-shadow:0 2px 8px rgba(0,0,0,.12)}
.page--cover{left:182px;top:62px;width:392px}
.page--one{left:626px;top:62px;width:388px}
.page--two{left:182px;top:658px;width:392px}
.page--three{left:626px;top:659px;width:388px}
.abs{position:absolute;display:block}

/* cover */
.brand{position:absolute;left:0;right:0;top:8px;text-align:center}
.brand-dot{width:62px;height:62px;border-radius:50%;background:var(--slate);margin:0 auto 10px}
.brand-name{font-family:"Cinzel",serif;font-weight:700;font-size:18px;letter-spacing:1px;color:var(--slate);line-height:1}
.brand-tagline{font-family:"Cinzel",serif;font-weight:700;font-size:8px;letter-spacing:.6px;color:var(--slate);margin-top:3px}
.cover-photo{position:absolute;left:0;top:131px;width:100%;height:213px;background:linear-gradient(90deg,#2c3a46 0%,#4c5b66 32%,#c9b98a 55%,#e9d59a 75%,#b9a15a 100%)}
.cover-photo::after{content:"";position:absolute;left:0;right:0;bottom:0;height:40%;background:linear-gradient(180deg,rgba(108,120,70,0),rgba(80,90,60,.55))}
.cover-title{position:absolute;left:0;right:0;top:372px;text-align:center;font-family:"Cinzel",serif;font-weight:700;font-size:29px;line-height:31.5px;color:var(--slate)}
.cover-footer{position:absolute;left:0;right:0;bottom:0;height:32px;background:var(--orange);color:#fff;font-family:"Cinzel",serif;font-weight:600;font-size:10.5px;letter-spacing:.6px;text-align:center;line-height:32px}

/* inner pages */
.intro{position:absolute;left:0;top:0;width:100%;height:91px;background:linear-gradient(90deg,#1f2520 0%,#3d4a3a 40%,#59614a 60%,#2d332c 100%)}
.intro-text{position:absolute;left:21px;right:21px;top:17px;color:#fff;font-style:italic;font-weight:700;font-size:8.1px;line-height:10.7px;text-align:justify}
.qa{position:absolute;left:18px;right:18px}
.qa-head{position:relative;padding-left:28px;min-height:20px;color:var(--orange);font-weight:700;font-size:7.3px;line-height:9px;display:flex;align-items:center}
.qa-icon{position:absolute;left:0;top:-1px;width:22px;height:22px;border-radius:50%;background:var(--orange);color:#fff;font-size:12px;font-weight:700;line-height:22px;text-align:center}
.qa-body{font-size:6.9px;line-height:9.1px;text-align:justify;margin-top:3px}
.page-foot{position:absolute;left:0;right:0;bottom:0;height:14px;background:var(--orange)}
.page-num{position:absolute;right:0;bottom:0;width:32px;height:14px;background:var(--slate);color:#fff;font-size:6.5px;font-weight:700;text-align:center;line-height:14px}
.top-strip{position:absolute;left:0;top:0;width:100%;height:8px}
.city-photo{position:absolute;left:0;bottom:14px;width:100%;height:122px;background:linear-gradient(180deg,#ffffff 0%,#e4e9ef 35%,#b9c4cf 70%,#6f7d8a 100%)}
.desk-photo{position:absolute;left:0;top:0;width:100%;height:190px;background:linear-gradient(180deg,#5b3f2c 0%,#7a5a40 45%,#c9b8a6 80%,#ffffff 100%)}
</style>
</head>
<body>

<section class="page page--cover">
  <div class="brand">
    <div class="brand-dot"></div>
    <div class="brand-name">TRAILMARK</div>
    <div class="brand-tagline">CHART YOUR VENTURE COURSE</div>
  </div>
  <svg class="abs" style="left:0;top:113px" width="392" height="18"><polygon points="118,0 392,0 392,18 104,18" fill="var(--slate)"/></svg>
  <div class="cover-photo" role="img" aria-label="Photo of a man pulling back a dark curtain to reveal a sunlit country road"></div>
  <svg class="abs" style="left:0;top:344px" width="392" height="18"><polygon points="0,0 282,0 268,18 0,18" fill="var(--slate)"/></svg>
  <h1 class="cover-title">10 Questions<br>To Choose The Best<br>Technology Advisor</h1>
  <div class="cover-footer">WWW.VENTURETRAILMARK-EXAMPLE.COM</div>
</section>

<section class="page page--one">
  <div class="intro" role="img" aria-label="Photo of a winding road through a forest"></div>
  <svg class="abs" style="left:0;top:0" width="388" height="12"><polygon points="0,0 388,0 388,12 0,12" fill="var(--slate)"/><polygon points="110,0 388,0 388,12 100,12" fill="var(--orange)"/></svg>
  <p class="intro-text">When you choose a technology advisor whether it be a Managed Service Provider, fractional CIO or a full-time CIO you need to make sure that they understand business just as much as they understand technology. Some of the biggest complaints about the IT department are that they just don’t “Get it”. The questions below should help you determine whether or not they have a technology mindset or a business mindset.</p>

  <div class="qa" style="top:97px">
    <div class="qa-head"><span class="qa-icon">?</span>What is scalability? How important is it from a technology perspective on a scale of 1-&gt;10 with 10 being the highest? What all does scalability impact?</div>
    <p class="qa-body">This question is designed to get a reading on the person’s mindset. A typical technology-minded response would be something describing the ability of systems or software to scale by adding additional resources. When working from a business point of view, however, you want to see it defined as the ability for the organization to support increased volume without sacrificing margins. The importance of this concept cannot be overstated and should be a 9 or 10 in terms of ranking. Regarding impact, you want to see not just an understanding of having to spend money two or three times for a different solution to the same problem, but an acknowledgment of the ‘total’ cost, including adoption fatigue, the opportunity cost of change, and the competitive disadvantage it creates. For concepts of business scalability refer to ‘Growing Past Limits’ by Dale Wrenfield.</p>
  </div>

  <div class="qa" style="top:217px">
    <div class="qa-head"><span class="qa-icon">?</span>Provide an example where you solved a problem without the use of technology.</div>
    <p class="qa-body">Often technology-minded individuals become so wrapped up in the solutions themselves they fail to realize a policy or process change is far more effective and simple than making changes to existing or introducing new technology. Asking for a specific example here should demonstrate the ability to think from a business mindset. For specific examples reference ‘The Ember Protocol’ by Hollis, Marek, and Tandy.</p>
  </div>

  <div class="qa" style="top:291px">
    <div class="qa-head"><span class="qa-icon">?</span>How do you go about prioritizing solutions in order of importance for implementation / adoption?</div>
    <p class="qa-body">Answers here should include reference to some form of discovery process or a thorough evaluation at the operations level. One of the key skill sets for someone approaching technology from a business point of view is mapping solutions and their respective importance to business outcomes and (often more importantly) eliminating bottlenecks while respecting that some implementations must necessarily come before others to be viable. For reference on the Theory of Constraints see ‘The Throughput’ by Aaron Veldmann.</p>
  </div>

  <div class="qa" style="top:380px">
    <div class="qa-head"><span class="qa-icon">?</span>What is Information Technology Debt?</div>
    <p class="qa-body">Stated simply, ‘IT Debt’ is a measurement of the out-of-date, incomplete or yet-to-be-defined technology changes. Debt occurs for a number of reasons, including lack of qualified personnel to implement the needed solutions (or recognize the problem in the first place); historical spending haunting the organization “we spent money on something like this before and look what it got us”; Fire-fighting (addressing issues purely reactively in a downward spiral leaving no time for fixing the root underlying problem); or most commonly, the budget being already allocated to other company endeavors that seem immediately more pressing. By recognizing what IT Debt is, the individual demonstrates a clear judgment of how impactful it can be when neglected and not brought to the forefront of business planning sessions</p>
  </div>

  <div class="page-foot"></div><div class="page-num">01</div>
</section>

<section class="page page--two">
  <svg class="top-strip" width="392" height="8"><rect width="392" height="8" fill="var(--slate)"/><polygon points="126,0 392,0 392,8 120,8" fill="var(--orange)"/></svg>

  <div class="qa" style="top:43px;left:22px;right:22px">
    <div class="qa-head"><span class="qa-icon">?</span>Provide an example where you argued against implementing a technology solution and why.</div>
    <p class="qa-body">Despite it being seemingly obvious, using ‘outside of budget’ is not a good answer. Business-minded technology advisors should be intimately aware of how well a proposed solution will integrate into the existing company ecosystem (software tools already present, workflow, and processes), if it drives the company toward reducing/eliminating a bottleneck (and thereby creates more leverage), and if it fits the company’s culture. If any of these are a no, the solution should be carefully examined for what it really offers the organization. If yes, the budget should be evaluated as a cost-benefit analysis, not a flat number ‘not to exceed’.</p>
  </div>

  <div class="qa" style="top:152px;left:22px;right:22px">
    <div class="qa-head"><span class="qa-icon">?</span>What is your ideal method for maintaining technology alignment for the company?</div>
    <p class="qa-body">You want to see a specific process envisioned here. At the very least a recommendation to be involved in business planning meetings or retreats, and ideally a standing technology focused meeting with leadership present should be argued for. For technology to be truly in alignment, it must fit the needs of the organization, not the other way around. This needs to come from the top level, and it means a representative must be present in critical business strategy meetings to understand where the company is headed, what operational constraints they are encountering, and what their short-term goals are. For an outline of how this model has been the underlying key to success for several well-known companies reference ‘Steady to Standout’ by Rhea Castellan.</p>
  </div>

  <div class="qa" style="top:265px;left:22px;right:22px">
    <div class="qa-head"><span class="qa-icon">?</span>How do you plan on measuring and monitoring the adoption success of a solution or project?</div>
    <p class="qa-body">Technically minded individuals often look at the point of ‘it’s up and running and it all works’, as where their responsibilities end. Someone with a business mindset should demonstrate that evaluating how well the solution has been adopted into the day to day workflow, and to what degree the solution has increased leverage or operational transparency are the true critical indicators of success. There should be a specific process of follow-up after implementation to flag adoption or workflow issues due to problems such as inadequate training, unforeseen incompatibilities (whether they be process or technology related), or simply resistance to change. These findings can then be brought back to leadership to evaluate how best to improve successful adoption going</p>
  </div>

  <div class="city-photo" role="img" aria-label="Photo of city skyscrapers rising above low clouds"></div>
  <div class="page-foot"></div><div class="page-num">02</div>
</section>

<section class="page page--three">
  <div class="desk-photo" role="img" aria-label="Photo of a wooden desk with a laptop, coffee and a sheet of hand-drawn business sketches"></div>

  <div class="qa" style="top:200px">
    <div class="qa-head"><span class="qa-icon">?</span>Provide an example where you had to balance customer and employee technology experience with security and compliance.</div>
    <p class="qa-body">A critical role fulfilled by a technology advisor is being able to balance maintaining compliance and sound security practices with as painless of a technology experience as possible. They should be able to weigh the critical importance of protecting the organization from the negative public relations and liability of a security flaw while respecting a solution must be usable to be useful. Look for an example that demonstrates an understanding of both sides and strikes a balance without going to an extreme in either direction.</p>
  </div>

  <div class="qa" style="top:300px">
    <div class="qa-head"><span class="qa-icon">?</span>What would you do first, if you were selected as our advisor? Can you give me details on what your discovery or on-boarding process includes?</div>
    <p class="qa-body">You are looking to make sure that they don’t stop at the technology. There should be a higher focus on understanding what the company processes are and how the people inside the organization get work done. If they focus only on network, security, and disaster recovery assessments then they do not have a business mindset.</p>
  </div>

  <div class="qa" style="top:374px">
    <div class="qa-head"><span class="qa-icon">?</span>Can you give me an example of a time you gave a suggestion for a solution and it was not taken? Describe the solution and why it was important to the organization. And why do you think they didn’t implement it?</div>
    <p class="qa-body">When they describe why they think the solution was important do they simply talk about risk reduction or uptime improvements without tying them back to an organizational goal or bottleneck. Being able to demonstrate actual business value is a critical skill for a technology advisor. For reference on technical excellence in service of business objectives rather than blindly servicing requirements read ‘A Chair in The Boardroom’ by Lionel Hargrove.</p>
  </div>

  <div class="page-foot"></div><div class="page-num">03</div>
</section>

</body>
</html>
```